Cartwell - custom section required

Hi, I am preparing a new cartwell site (not yet active).

I want to add a section to a theme that will need to be built from liquid or HTLM or any way that works. This section will be part of the home page. This section will be for information purposes only. The section would help with explain about an outsole, my idea would to be exactly like a premium tyre shop advertises. see link. https://www.vandoro.com/tyres/en-au/car/catalogue/product/falcon-gtx
I have attached my mock up of how the section could look. I am looking for someone to code this section with the interactivity like the tyre site. For example: 1) see the sliders how the come across when you scroll down, with our different properties customised. 2) The image windows with the different angles being nicely interactive ti show largewr image when hovering over. 3) If we could do like they did when you press on the different part of the tyre (for our site it would be the outsole) how it lights up the areas and talks about the properties of that area. So our outsole different parts would light up with different explanations.

This section is a quirky idea but will only really work if it is interactive and very professional. It would be great if the content could be modified without too much difficulty. The section could be different to my mock up, creative ideas that contribute to the feel of this section are welcome.

The design must be compatible with Cartwell so I can just easily drop the code in to create the section.

Target Market(s)

Trendy people

Industry/Entity Type

Fashion

Coding

Coded - Design and coding required

Number of Pages Required

1 page

Requirements
Must have
• Must have responsiveness and animated as described.
Nice to have
• If the branding could be included it would be great.

```html
<!DOCTYPE html>
<html lang="en">
<head>
<meta charset="utf-8">
<title>Kinfolk Tread Performance Pro Outsole</title>
<link href="https://fonts.googleapis.com/css2?family=Montserrat:wght@400;500;600;700;800&display=swap" rel="stylesheet">
<style>
:root{
  --brand:#3b5a8a;
  --brand-dark:#2f4a78;
  --ink:#222;
  --muted:#6a6a6a;
  --line:#d6d6d6;
  --bar-on:#7a7a7a;
  --bar-off:#c9c9c9;
  --sole:#8a8d90;
  --footer:#7f858a;
  --white:#fff;
}
*{box-sizing:border-box;margin:0;padding:0}
html,body{width:1200px;height:2833px;overflow:hidden;background:var(--white)}
body{position:relative;font-family:'Montserrat',sans-serif;color:var(--ink)}
.abs{position:absolute}
.topline{left:0;top:0;width:1200px;height:4px;background:var(--brand)}
.logo{left:112px;top:36px;font-size:23px;font-weight:800;color:var(--ink)}
.nav a{position:absolute;top:43px;font-size:15px;font-weight:500;color:var(--ink);text-decoration:none}
.hero{left:0;top:101px;width:1200px;height:376px;background:linear-gradient(120deg,#5b77a3,#45628f 55%,#3d5987)}
.hero h1{position:absolute;width:100%;top:160px;text-align:center;font-size:46px;font-weight:800;color:var(--white);letter-spacing:.5px}
.crumb{left:112px;top:520px;font-size:15px;color:#444}
.crumb b{color:var(--brand);font-weight:600}
.ph{background:linear-gradient(160deg,#a3a6a9,#7e8285);border-radius:10px}
.thumb-label{font-size:10px;color:#aaa;text-align:center;width:88px}
.main-frame{left:235px;top:585px;width:338px;height:340px;border-radius:14px;box-shadow:0 2px 10px rgba(0,0,0,.08);background:#fff}
.title{left:620px;top:582px;font-size:27px;font-weight:800;color:var(--brand);line-height:30px}
.desc{left:621px;top:655px;width:420px;font-size:11px;line-height:18px;color:#555}
.qty{left:621px;top:747px;width:37px;height:37px;border:1px solid var(--line);border-radius:8px;font-size:10px;color:#777;padding:12px 0 0 6px}
.cart-btn{left:672px;top:746px;width:173px;height:38px;border-radius:19px;background:var(--brand);color:#fff;font-weight:700;font-size:15px;text-align:center;line-height:38px}
.label-size{left:621px;top:803px;font-size:15px;font-weight:700;color:var(--brand)}
.size{position:absolute;width:29px;height:29px;border:1px solid var(--line);border-radius:3px;font-size:13px;text-align:center;line-height:27px;color:#555}
.size.on{background:var(--brand);border-color:var(--brand);color:#fff}
.divider{left:621px;top:880px;width:450px;height:1px;background:#bbb}
.use{position:absolute;top:995px;text-align:center;font-size:7.5px;color:#666;width:70px}
.use .ico{width:36px;height:36px;margin:0 auto 8px;border-radius:50%;background:#b9bcbf}
.h2{position:absolute;left:112px;font-size:19px;font-weight:800;color:var(--brand)}
.lead{left:113px;top:1124px;font-size:15px;font-weight:500;color:#111}
.body-text{left:113px;top:1158px;width:930px;font-size:13px;line-height:23px;color:#666}
.perf-row{position:absolute;left:112px;width:800px;height:20px}
.perf-row span{position:absolute;left:0;top:0;font-size:13.5px;font-weight:500;color:#555;letter-spacing:.3px}
.bars{position:absolute;left:162px;top:8px;display:flex;gap:7.6px}
.bars i{display:block;width:56px;height:2px;background:var(--bar-off)}
.bars i.on{height:3px;background:var(--bar-on)}
.sub{left:112px;top:1675px;font-size:15px;font-weight:500;color:#666}
.hotspot{position:absolute;width:38px;height:38px;border-radius:50%;background:#fff;box-shadow:0 2px 6px rgba(0,0,0,.3);color:#666;font-weight:700;font-size:22px;text-align:center;line-height:37px}
.tip{left:393px;top:1924px;width:218px;height:112px;background:var(--brand);border-radius:3px;color:#fff;font-size:8.5px;font-weight:600;line-height:15px;padding:26px 20px 0 41px;text-transform:uppercase}
.details-text{left:112px;top:2180px;width:480px;font-size:12px;line-height:19px;color:#777}
.footer{left:0;top:2286px;width:1200px;height:547px;background:linear-gradient(180deg,#7e848a,#80868b 60%,#777d82)}
.fline{position:absolute;left:112px;width:975px;height:2px;background:#e8e8e8}
.sub-h{left:112px;top:2396px;font-size:23px;font-weight:800;color:#fff}
.sub-p{left:112px;top:2443px;font-size:15px;color:#f0f0f0}
.email{left:541px;top:2405px;width:349px;height:50px;background:#fff;border-radius:4px;font-size:14px;color:#777;padding:16px 0 0 30px}
.sub-btn{left:897px;top:2405px;width:190px;height:50px;background:var(--brand);border-radius:4px;color:#fff;font-weight:700;font-size:17px;text-align:center;line-height:50px}
.col{position:absolute;top:2555px;color:#fff}
.col h3{font-size:26px;font-weight:800;margin-bottom:20px}
.col a{display:block;font-size:19px;color:#f2f2f2;text-decoration:none;line-height:30px;margin-left:2px}
.copy{left:0;top:2787px;width:1200px;text-align:center;font-size:13px;color:#f2f2f2}
</style>
</head>
<body>
<div class="abs topline"></div>
<div class="abs logo">Kinfolk Tread</div>
<nav class="nav">
  <a style="left:485px">Home</a><a style="left:579px">About Us</a><a style="left:699px">Products</a><a style="left:816px">Shop</a><a style="left:904px">Contact Us</a>
</nav>
<svg class="abs" style="left:1022px;top:39px" width="26" height="26" viewBox="0 0 26 26"><circle cx="13" cy="13" r="11.5" fill="none" stroke="#222" stroke-width="2"/><circle cx="13" cy="10" r="4" fill="#222"/><path d="M6 20c2-4 12-4 14 0" fill="#222"/></svg>
<svg class="abs" style="left:1065px;top:41px" width="24" height="22" viewBox="0 0 24 22"><path d="M1 2h4l3 12h12l3-9H7" fill="none" stroke="#222" stroke-width="2.2"/><path d="M7 5h15l-3 9H9z" fill="#222"/><circle cx="10" cy="19" r="2" fill="#222"/><circle cx="18" cy="19" r="2" fill="#222"/></svg>

<section class="abs hero" role="img" aria-label="Photo of a runner's shoes on a track, tinted blue"><h1>SHOP OUR PRODUCTS</h1></section>

<div class="abs crumb">Outsole/ Catagory/ <b>Performance Pro Outsole</b></div>

<div class="abs ph" style="left:114px;top:585px;width:84px;height:106px" role="img" aria-label="Outsole pair, top view"></div>
<div class="abs thumb-label" style="left:112px;top:704px">Sole view</div>
<div class="abs ph" style="left:114px;top:752px;width:84px;height:40px" role="img" aria-label="Outsole, angled view"></div>
<div class="abs thumb-label" style="left:112px;top:802px">Side view</div>
<div class="abs ph" style="left:114px;top:850px;width:76px;height:26px" role="img" aria-label="Outsole, side profile"></div>
<div class="abs thumb-label" style="left:112px;top:888px">Heel view</div>

<div class="abs main-frame">
  <div class="abs ph" style="left:60px;top:33px;width:218px;height:275px;border-radius:90px 90px 60px 60px" role="img" aria-label="Large image of the outsole pair from below"></div>
</div>

<div class="abs title">Kinfolk Tread<br>Performance Pro Outsole</div>
<p class="abs desc">Premium design for an appealing finish to your multipurpose boots. The Performance Pro outsole has a unique high contrast side view with a velvet touch. The Branding&nbsp; adds a stylish finish for a boot that looks as good as it performs.</p>
<div class="abs qty">01 ⇕</div>
<div class="abs cart-btn">Add To Cart</div>
<div class="abs label-size">Choose Size</div>
<div class="size on" style="left:621px;top:838px">14</div>
<div class="size on" style="left:659px;top:838px">20</div>
<div class="abs divider"></div>
<div class="size" style="left:621px;top:897px">16</div>
<div class="size" style="left:661px;top:897px">18</div>
<div class="size" style="left:702px;top:897px">22</div>
<div class="size" style="left:743px;top:897px">24</div>
<div class="size" style="left:784px;top:897px">26</div>
<div class="size" style="left:824px;top:897px">30</div>

<div class="use" style="left:106px"><div class="ico" role="img" aria-label="All weather icon"></div>ALL WEATHER</div>
<div class="use" style="left:193px"><div class="ico" role="img" aria-label="Glamping icon"></div>GLAMPING</div>
<div class="use" style="left:273px"><div class="ico" role="img" aria-label="Clubbing icon"></div>CLUBBING</div>
<div class="use" style="left:351px"><div class="ico" role="img" aria-label="Festivals icon"></div>FESTIVALS</div>

<h2 class="h2" style="top:1083px">Performance Pro Outsole</h2>
<p class="abs lead">All weather is welcome. Designed for rugged seasons and unexpected kneesup.</p>
<p class="abs body-text">Kinfolk Tread Performance Pro is a high performance outsole that features an asymmetrical tread pattern and tread rigidity which ensures the best grip on wet surfaces, and outstanding handling performance on grassed areas. Dynamic Response technology optimizes dance precision for optimum grooves, from city clubs to wet field days.</p>

<h2 class="h2" style="top:1257px">Performance</h2>
<div class="perf-row" style="top:1306px"><span>DRY</span><div class="bars"><i class="on"></i><i class="on"></i><i class="on"></i><i class="on"></i><i class="on"></i><i class="on"></i><i class="on"></i><i class="on"></i><i></i><i></i></div></div>
<div class="perf-row" style="top:1350px"><span>WET</span><div class="bars"><i class="on"></i><i class="on"></i><i class="on"></i><i class="on"></i><i class="on"></i><i class="on"></i><i class="on"></i><i class="on"></i><i class="on"></i><i class="on"></i></div></div>
<div class="perf-row" style="top:1394px"><span>CLUBBING</span><div class="bars"><i class="on"></i><i class="on"></i><i class="on"></i><i class="on"></i><i class="on"></i><i class="on"></i><i class="on"></i><i class="on"></i><i class="on"></i><i></i></div></div>
<div class="perf-row" style="top:1437px"><span>BARS</span><div class="bars"><i class="on"></i><i class="on"></i><i class="on"></i><i class="on"></i><i class="on"></i><i class="on"></i><i class="on"></i><i class="on"></i><i class="on"></i><i></i></div></div>
<div class="perf-row" style="top:1481px"><span>MUSIC FESTIVALS</span><div class="bars"><i class="on"></i><i class="on"></i><i class="on"></i><i class="on"></i><i class="on"></i><i class="on"></i><i class="on"></i><i class="on"></i><i></i><i></i></div></div>
<div class="perf-row" style="top:1525px"><span>CLAMPING</span><div class="bars"><i class="on"></i><i class="on"></i><i class="on"></i><i class="on"></i><i class="on"></i><i class="on"></i><i class="on"></i><i class="on"></i><i class="on"></i><i></i></div></div>
<div class="perf-row" style="top:1569px"><span>ON POINT</span><div class="bars"><i class="on"></i><i class="on"></i><i class="on"></i><i class="on"></i><i class="on"></i><i class="on"></i><i class="on"></i><i class="on"></i><i class="on"></i><i></i></div></div>

<h2 class="h2" style="top:1631px">Homologation</h2>
<p class="abs sub">long established fact that a reader will be distracted</p>

<div class="abs" style="left:133px;top:1732px;width:135px;height:374px;border-radius:70px 70px 55px 55px;background:linear-gradient(180deg,#8f9296,#6f8db8 50%,#8f9296)" role="img" aria-label="Left outsole with highlighted blue tread grooves"></div>
<div class="abs" style="left:287px;top:1732px;width:135px;height:374px;border-radius:70px 70px 55px 55px;background:linear-gradient(180deg,#8f9296,#6f8db8 50%,#8f9296)" role="img" aria-label="Right outsole with highlighted blue tread grooves"></div>
<div class="abs tip">Lateral grooves for rapid water expulsion in wet conditions &amp; looking chic regardless of the event</div>
<div class="hotspot" style="left:113px;top:1848px">+</div>
<div class="hotspot" style="left:218px;top:1923px">+</div>
<div class="hotspot" style="left:331px;top:1750px">+</div>
<div class="hotspot" style="left:390px;top:1923px;color:var(--brand)">+</div>
<div class="hotspot" style="left:330px;top:2057px">+</div>

<h2 class="h2" style="top:2148px">Details</h2>
<p class="abs details-text">Lateral grooves for rapid water expulsion in wet conditions &amp; looking chic regardless of the event</p>

<footer class="abs footer" role="img" aria-label="Faded photo of runners' legs on a track behind the footer">
  <div class="fline" style="top:76px"></div>
  <div class="fline" style="top:214px"></div>
</footer>
<div class="abs sub-h">Subscribe to our newsletter</div>
<div class="abs sub-p">Get the latest news and updates</div>
<div class="abs email">Your Email Address</div>
<div class="abs sub-btn">Subscribe</div>
<div class="col" style="left:147px"><h3>Product</h3><a>Login</a><a>Product</a><a>Case studies</a><a>Pricing</a></div>
<div class="col" style="left:401px"><h3>Company</h3><a>About us</a><a>Contact us</a><a>Shop</a><a>Products</a></div>
<div class="col" style="left:676px"><h3>Follow us</h3><a>Crewlink</a><a>Friendwall</a><a>Photostream</a></div>
<div class="col" style="left:946px"><h3>Legal</h3><a>Privacy policy</a><a>Return</a><a>Terms</a></div>
<div class="abs copy">Copyright © 2022 | All Rights Reserved.</div>
</body>
</html>
```